Business card design for Velvet Harbor

We need business cards designed for our new marketing consulting company, Velvet Harbor. Our services include marketing strategy, go-to-market and launch planning, growth strategy, and execution. We serve medical technology and health technology companies, from startups to well-established growth companies.

The business cards should feel professional, credible, reliable and trustworthy, and should instill confidence. Also bold, creative, and modern.

The design must use the Velvet Harbor logo.

The primary brand color is this orange: #FF5501
A secondary color that you can use is this gray: #282B2D
I would prefer only to use the orange and gray. But if you feel you really need an additional accent color (please use it very sparingly, as little as possible), you can use this blue for small accent purposes: #009FED

Attached are the logo files. The main logo is the one with a little bit of orange on the left and the rest is gray.

The business card should include the following:

Velvet Harbor logo
First name and last name
Title
Email address
Phone number and type (in whatever order looks best for the design
Website (the website does not need to be in the same block as the personal info)

For example:

Nessa Pryle
Founder & Principal
nessa@velvetharbor.com
+1.628.309.4156 mobile (can use "." or spaces in between blocks of numbers)
velvetharbor.com (somewhere on the card, it does not need to be with the personal info; and note that there is no "www." at the beginning)

Note that there will be no address listed on the business card.

Target Market(s)

Executives (CEO, head of marketing, head of sales) at medical technology and health technology companies, mostly in their 40s and older, well-educated, often with advanced degrees. They are strategic thinkers, responsible for budgets, and familiar with P&L. Their comfort with and trust in using outside consultants varies.

Industry/Entity Type

Medical technology and health technology companies.

Contact Information for Business Card

See project description

Font styles to use
Sans Serif

Requirements
Must have
• Logo and see Business card details section above.

```html
<!DOCTYPE html>
<html lang="en">
<head>
<meta charset="utf-8">
<title>Velvet Harbor — Business Card Concepts</title>
<link rel="stylesheet" href="https://fonts.googleapis.com/css2?family=Lato:wght@400;700&display=swap">
<style>
  :root {
    --orange: #FF5501;
    --graphite: #282B2D;
    --white: #FFFFFF;
    --backdrop: #F0F1F3;
  }
  * { margin: 0; padding: 0; box-sizing: border-box; }
  html, body {
    width: 827px; height: 1200px; overflow: hidden;
    background: var(--backdrop);
    font-family: "Lato", "Helvetica Neue", Arial, sans-serif;
  }
  .sheet { position: relative; width: 827px; height: 1200px; }

  .card {
    position: absolute; left: 180px; width: 467px; height: 267px;
    overflow: hidden;
    box-shadow: 0 18px 30px rgba(0,0,0,0.16), 0 4px 10px rgba(0,0,0,0.06);
  }
  .card--light  { top: 95px;  background: var(--white); }
  .card--dark   { top: 436px; background: var(--graphite); }
  .card--bright { top: 800px; background: var(--orange); }

  .brand {
    position: absolute; left: 33px; top: 118px;
    display: flex; align-items: center; gap: 10px;
  }
  .brand__dot { width: 22px; height: 22px; border-radius: 50%; background: var(--orange); }
  .brand__name {
    font-weight: 700; font-size: 14px; line-height: 15px;
    letter-spacing: 4.2px; text-transform: uppercase;
  }
  .website {
    position: absolute; left: 53px; top: 228px;
    font-size: 14.6px; letter-spacing: 0.3px;
  }
  .base-bar {
    position: absolute; left: 0; bottom: 0; width: 234px; height: 15px;
    border-top-right-radius: 6px;
  }

  .contact-panel {
    position: absolute; left: 234px; top: 26px; right: 0; height: 214px;
    border-bottom-left-radius: 10px;
  }
  .person { position: absolute; left: 19px; top: 21px; }
  .person__name { font-size: 22px; line-height: 24px; font-weight: 400; }
  .person__name b { font-weight: 700; }
  .person__title { font-size: 11.5px; margin-top: 3px; letter-spacing: 0.2px; }
  .reach {
    position: absolute; left: 19px; top: 153px;
    font-size: 16.5px; line-height: 21.5px; letter-spacing: 0.2px;
  }

  /* colourways */
  .card--light .brand__name { color: var(--graphite); }
  .card--light .website { color: var(--graphite); }
  .card--light .base-bar { background: var(--graphite); }
  .card--light .contact-panel { background: var(--orange); color: var(--white); }

  .card--dark .brand__name { color: var(--white); }
  .card--dark .website { color: var(--white); }
  .card--dark .base-bar { background: var(--orange); }
  .card--dark .contact-panel { background: var(--white); color: var(--graphite); }
  .card--dark .person__name { color: var(--orange); }

  .card--bright .brand__name { color: var(--white); }
  .card--bright .brand__dot { background: var(--white); }
  .card--bright .website { color: var(--white); }
  .card--bright .base-bar { background: var(--graphite); }
  .card--bright .contact-panel { background: var(--white); color: var(--graphite); }
</style>
</head>
<body>
<main class="sheet">

  <section class="card card--light">
    <div class="brand"><span class="brand__dot"></span><span class="brand__name">Velvet<br>Harbor</span></div>
    <p class="website">velvetharbor.com</p>
    <div class="base-bar"></div>
    <div class="contact-panel">
      <div class="person">
        <h2 class="person__name"><b>Nessa</b> Pryle</h2>
        <p class="person__title">Founder &amp; Principal</p>
      </div>
      <p class="reach">+1 628 309 4156<br>nessa@velvetharbor.com</p>
    </div>
  </section>

  <section class="card card--dark">
    <div class="brand"><span class="brand__dot"></span><span class="brand__name">Velvet<br>Harbor</span></div>
    <p class="website">velvetharbor.com</p>
    <div class="base-bar"></div>
    <div class="contact-panel">
      <div class="person">
        <h2 class="person__name"><b>Nessa</b> Pryle</h2>
        <p class="person__title">Founder &amp; Principal</p>
      </div>
      <p class="reach">+1 628 309 4156<br>nessa@velvetharbor.com</p>
    </div>
  </section>

  <section class="card card--bright">
    <div class="brand"><span class="brand__dot"></span><span class="brand__name">Velvet<br>Harbor</span></div>
    <p class="website">velvetharbor.com</p>
    <div class="base-bar"></div>
    <div class="contact-panel">
      <div class="person">
        <h2 class="person__name"><b>Nessa</b> Pryle</h2>
        <p class="person__title">Founder &amp; Principal</p>
      </div>
      <p class="reach">+1 628 309 4156<br>nessa@velvetharbor.com</p>
    </div>
  </section>

</main>
</body>
</html>
```